Bramblewick Acres Organic Hemp Company needs an OLD WORLD Label for CBD Bottle!

*UPDATE* Increased the budget! Please keep in mind, we are also open to "modern vintage", "hipster vintage" and other forms of retro emulation. Whatever the case, we are looking for a small work of art, like an indie Gin bottle- not the clinical drab that every other CBD bottle has. Also, don't be afraid to incorporate color, or alter the logo (color wise), we want something breathtaking in a small package. Show us what that looks like to you!

*UPDATE* Please take a moment to visit this link to see the types of branding we are interested in: https://www.pinboardly.example/tobiasquentinharlow/neat-branding/

We are an Organic Hemp company about to launch it's first line of products. This design is for our CBD Bottle. We have a pre-existing logo that we need developed and expanded into a label. Our theme is Old World, Victorian, Vintage, Turn of the Century (there are too many names for this genre, you get it...) We want our brand to convey a sense of intrigue, artisan quality and a bit of mystery. Very different from the clinical look of most CBD tinctures. We are HUGE fans of the design house "Copper and Copper" and would LOVE something that conjures that feel.

The first attachment will be our current logo, and I will be adding "inspiration" as I can.

The second attachment will be a rendition of our raw logo with regulatory information. This is what we need this spiced up! You DO NOT have to follow this design, but the same information needs to be on there. It's very likely that the line work will be in "gold foil".

Any additional attachments are for "inspiration", what we're looking for.

Feel free to explore with it, we are looking for something breathtaking!

Thanks!

Tobias
Bramblewick Acres
Verdant Curios

Target Market(s)

Younger, Hipster Demographic and all who are interested in Organic Products!

Colors

Designer to choose colors to be used in the design.

Requirements
Must have
• Full Spectrum Hemp Extract CDB Oil 1000mg Natural Flavor 1.02 FL OZ (30 ML)
Should not have
• Cannabis, Cannabis leaves, Marijuana etc...

```html
<!DOCTYPE html>
<html lang="en">
<head>
<meta charset="utf-8">
<title>Bramblewick Acres – CDB Oil Label</title>
<link rel="stylesheet" href="https://fonts.googleapis.com/css2?family=Playfair+Display:wght@700&family=Oswald:wght@500;600&display=swap">
<style>
  :root {
    --page: #ffffff;
    --label-black: #0b0b0a;
    --gold: #b89a5a;
    --gold-soft: rgba(184, 154, 90, 0.35);
    --gold-deep: #6b5226;
    --sage: #9fc3b4;
    --sage-band: #a9cbbd;
    --ivory: #f2f0ea;
    --ink: #1a1a18;
  }
  html, body {
    margin: 0;
    padding: 0;
    width: 1200px;
    height: 1044px;
    overflow: hidden;
    background: var(--page);
  }
  .canvas {
    position: relative;
    width: 1200px;
    height: 1044px;
  }
  .label {
    position: absolute;
    left: 280px;
    top: 52px;
    width: 640px;
    height: 940px;
    display: block;
  }
  .serif { font-family: "Playfair Display", Georgia, serif; font-weight: 700; }
  .sans { font-family: "Oswald", "Arial Narrow", sans-serif; font-weight: 600; }
  .brand-name { fill: var(--ivory); }
  .arc-small { fill: var(--sage); font-size: 15px; letter-spacing: 2px; }
  .estd { fill: var(--ivory); font-size: 12px; letter-spacing: 1px; }
  .ribbon-text { fill: var(--ink); font-size: 19px; letter-spacing: 3px; }
  .spectrum { fill: var(--sage); font-size: 25px; letter-spacing: 4px; }
  .product { fill: var(--gold-deep); font-size: 58px; }
  .strength { fill: var(--sage); font-size: 38px; letter-spacing: 7px; }
  .volume { fill: var(--ivory); font-size: 21px; letter-spacing: 2px; }
  .flavor { fill: var(--sage); font-size: 30px; letter-spacing: 6px; }
  .gold-line { fill: none; stroke: var(--gold); stroke-width: 2; }
  .gold-hair { fill: none; stroke: var(--gold); stroke-width: 1; }
</style>
</head>
<body>
<main class="canvas">
  <svg class="label" viewBox="0 0 640 940" xmlns="http://www.w3.org/2000/svg">
    <defs>
      <radialGradient id="rayGlow" cx="50%" cy="100%" r="90%">
        <stop offset="0" stop-color="#b89a5a" stop-opacity="0.35"/>
        <stop offset="1" stop-color="#b89a5a" stop-opacity="0"/>
      </radialGradient>
      <linearGradient id="scrollTone" x1="0" y1="0" x2="1" y2="0">
        <stop offset="0" stop-color="#b89a5a" stop-opacity="0.22"/>
        <stop offset="1" stop-color="#b89a5a" stop-opacity="0.04"/>
      </linearGradient>
      <path id="arcTop" d="M78,360 A86,86 0 0 1 215,250"/>
      <path id="arcVolume" d="M180,770 Q320,845 460,770"/>
      <path id="arcFlavor" d="M110,800 Q320,920 530,800"/>
    </defs>

    <!-- label ground -->
    <rect class="label-ground" x="0" y="0" width="640" height="940" fill="var(--label-black)"/>

    <!-- outer frame -->
    <path class="gold-line frame-outer" d="M24,260 L24,150 Q24,110 70,100 Q320,20 570,100 Q616,110 616,150 L616,260 L600,270 L600,680 L616,690 L616,790 Q616,830 570,840 Q320,930 70,840 Q24,830 24,790 L24,690 L40,680 L40,270 Z"/>
    <path class="gold-hair frame-inner" d="M38,258 L38,156 Q38,122 78,112 Q320,36 562,112 Q602,122 602,156 L602,258"/>

    <!-- sunburst area -->
    <ellipse role="img" aria-label="Fine gold sunburst rays fanning out above the brand name" cx="320" cy="230" rx="230" ry="150" fill="url(#rayGlow)"/>

    <!-- scroll flourishes -->
    <rect role="img" aria-label="Gold filigree scrollwork on the left side" x="44" y="380" width="120" height="170" rx="20" fill="url(#scrollTone)"/>
    <rect role="img" aria-label="Gold filigree scrollwork on the right side" x="476" y="320" width="120" height="200" rx="20" fill="url(#scrollTone)" transform="scale(-1,1) translate(-1072,0)"/>

    <!-- arc tagline -->
    <text class="sans arc-small"><textPath href="#arcTop">ORGANIC ARTISANAL HEMP</textPath></text>
    <text class="sans estd" x="150" y="300" text-anchor="middle">ESTD</text>
    <text class="sans estd" x="150" y="316" text-anchor="middle">2019</text>

    <!-- brand name -->
    <text class="serif brand-name" x="330" y="385" text-anchor="middle" font-size="64">Bramblewick</text>
    <text class="serif brand-name" x="300" y="445" text-anchor="middle" font-size="42">Acres</text>
    <circle class="gold-line brand-mark" cx="500" cy="440" r="44"/>

    <!-- ribbon -->
    <path class="ribbon" d="M100,500 L120,486 L530,486 L546,500 L530,528 L120,528 Z" fill="var(--ivory)"/>
    <text class="sans ribbon-text" x="325" y="514" text-anchor="middle">VERDANT CURIOS</text>
    <line x1="420" y1="542" x2="560" y2="542" stroke="var(--ivory)" stroke-width="3" stroke-dasharray="2 6" stroke-linecap="round"/>

    <!-- product block -->
    <line class="gold-line" x1="40" y1="558" x2="600" y2="558"/>
    <text class="sans spectrum" x="320" y="592" text-anchor="middle">FULL SPECTRUM HEMP EXTRACT</text>
    <line class="gold-hair" x1="40" y1="606" x2="600" y2="606"/>
    <rect class="product-band" x="40" y="610" width="560" height="66" fill="var(--sage-band)"/>
    <line class="gold-hair" x1="40" y1="680" x2="600" y2="680"/>
    <path d="M56,643 L150,643 M150,638 L162,643 L150,648" stroke="var(--ink)" stroke-width="2" fill="none"/>
    <path d="M584,643 L490,643 M490,638 L478,643 L490,648" stroke="var(--ink)" stroke-width="2" fill="none"/>
    <text class="serif product" x="320" y="664" text-anchor="middle">CDB OIL</text>

    <text class="sans strength" x="325" y="735" text-anchor="middle">1000MG</text>
    <path class="gold-hair" d="M110,710 Q150,740 200,725 M530,710 Q490,740 440,725"/>

    <!-- bottom arcs -->
    <path class="gold-hair" d="M150,750 Q320,830 490,750"/>
    <text class="sans volume"><textPath href="#arcVolume" startOffset="50%" text-anchor="middle">1.02 FL OZ (30 ML)</textPath></text>
    <text class="sans flavor"><textPath href="#arcFlavor" startOffset="50%" text-anchor="middle">NATURAL FLAVOR</textPath></text>
  </svg>
</main>
</body>
</html>
```